Business and Success Coaching Business Card

Need a business card for my coaching business. I coach small businesses, career professionals and, individuals wanting to unlock their human potential and achieve excellence. At the heart of our methodology is the Shaping Purposeful Action Routines Knowingly (SPARK) approach to formulate empowerment, create principles for success and setting achievable outcomes. I would like something that incorporates our new logo, something clean and sharp with a solid darker, but complementary background, color on the card front. The back should be white where there will be room for three questions

Target Market(s)

People looking to advance and improve themselves through a success coach

Industry/Entity Type

Life Coaching

Contact Information for Business Card

Contact information on card.
Business name on front of card
Questions on back

Font styles to use
Other font styles liked:
• Century Gothic or other Serif style fonts that look similar to Century Gothic

Colors

Designer to choose colors to be used in the design.

Requirements
Must have
• Logo on front of card
• Business name - The Steady Forge
• Contact name - Ted Harlow
• Address - Box 4619, Millbrook, VT 05799-4619
• Phone number - 303-555-0147
• Email address - harlow.ted@thesteadyforge.example
• Certifications - CPC, CLHt, ATT, PNCP
• Back of card
• Three questions on the back of the card:
• If you were at your best, what would you do right now?
• What is the decision you have been avoiding?
• What's one action you could take in the next 10 minutes?
Nice to have
• I would like to see a solid color on the front of the card that compliments the logo.
• Back should be white, or could be contrasting, but need to have the three questions.

```html
<!DOCTYPE html>
<html lang="en">
<head>
<meta charset="utf-8">
<title>The Steady Forge – Business Card</title>
<link rel="stylesheet" href="https://fonts.googleapis.com/css2?family=Roboto:wght@400;500;700&display=swap">
<style>
  :root {
    --stage: #223869;
    --navy: #1f346a;
    --white: #ffffff;
    --sky: #8fa9d8;
    --shadow: rgba(8, 18, 45, 0.35);
  }
  * { box-sizing: border-box; margin: 0; padding: 0; }
  html, body { width: 1200px; height: 800px; overflow: hidden; }
  body {
    background: var(--stage);
    font-family: "Roboto", Arial, sans-serif;
    position: relative;
  }
  .card {
    position: absolute;
    width: 454px;
    height: 282px;
    overflow: hidden;
    box-shadow: 0 2px 6px var(--shadow);
  }
  .card--tl { left: 130px; top: 105px; }
  .card--tr { left: 609px; top: 105px; }
  .card--bl { left: 130px; top: 417px; }
  .card--br { left: 609px; top: 417px; }

  /* Front */
  .card-front { background: var(--navy); color: var(--white); }
  .front-arc {
    position: absolute;
    left: -91px;
    top: -140px;
    width: 302px;
    height: 302px;
    border-radius: 50%;
    background: var(--white);
  }
  .brand {
    position: absolute;
    left: 18px;
    top: 44px;
    width: 160px;
    text-align: center;
  }
  .brand-dot {
    display: block;
    width: 30px;
    height: 30px;
    margin: 0 auto 9px;
    border-radius: 50%;
    background: var(--navy);
  }
  .brand-name {
    color: var(--navy);
    font-weight: 700;
    font-size: 14.5px;
    white-space: nowrap;
  }
  .brand-tagline {
    margin-top: 1px;
    color: var(--sky);
    font-size: 9px;
    white-space: nowrap;
  }
  .holder {
    position: absolute;
    right: 37px;
    top: 38px;
    text-align: right;
  }
  .holder-name { font-size: 19px; font-weight: 500; }
  .holder-credentials { margin-top: 4px; font-size: 8.5px; font-weight: 700; }
  .contacts {
    position: absolute;
    right: 37px;
    top: 182px;
    list-style: none;
  }
  .contact {
    display: flex;
    justify-content: flex-end;
    align-items: center;
    gap: 7px;
    height: 21.5px;
    font-size: 11.5px;
    white-space: nowrap;
  }
  .contact-icon { width: 12px; height: 12px; flex: none; }

  /* Back */
  .card-back { background: var(--white); }
  .questions {
    position: absolute;
    left: 0; right: 0; top: 86px;
    display: flex;
    justify-content: center;
    gap: 12px;
    list-style: none;
  }
  .question {
    width: 111px;
    height: 111px;
    border-radius: 50%;
    background: var(--navy);
    color: var(--white);
    display: flex;
    align-items: center;
    justify-content: center;
    text-align: center;
    font-size: 9px;
    font-weight: 500;
    line-height: 1.5;
    white-space: nowrap;
  }
</style>
</head>
<body>

<svg width="0" height="0" style="position:absolute" aria-hidden="true">
  <defs>
    <symbol id="icon-phone" viewBox="0 0 12 12">
      <circle cx="6" cy="6" r="6" fill="#ffffff"/>
      <path d="M4 3.2 L5 3 L5.6 4.6 L5 5.1 Q5.6 6.4 6.9 7 L7.4 6.4 L9 7 L8.8 8 Q8.5 8.8 7.6 8.7 Q4 8 3.3 4.4 Q3.2 3.5 4 3.2Z" fill="#1f346a"/>
    </symbol>
    <symbol id="icon-mail" viewBox="0 0 12 12">
      <circle cx="6" cy="6" r="6" fill="#ffffff"/>
      <rect x="3" y="3.8" width="6" height="4.4" rx="0.5" fill="#1f346a"/>
      <path d="M3.2 4 L6 6.2 L8.8 4" stroke="#ffffff" stroke-width="0.7" fill="none"/>
    </symbol>
    <symbol id="icon-pin" viewBox="0 0 12 12">
      <circle cx="6" cy="6" r="6" fill="#ffffff"/>
      <path d="M6 2.6 Q8.4 2.6 8.4 5 Q8.4 6.6 6 9.6 Q3.6 6.6 3.6 5 Q3.6 2.6 6 2.6Z" fill="#1f346a"/>
      <circle cx="6" cy="5" r="0.9" fill="#ffffff"/>
    </symbol>
  </defs>
</svg>

<section class="card card-back card--tl">
  <ul class="questions">
    <li class="question">If you were at your best,<br>what would<br>you do right now?</li>
    <li class="question">What is the decision<br>you have<br>been avoiding?</li>
    <li class="question">What's one action you<br>could take<br>in the next 10 minutes?</li>
  </ul>
</section>

<section class="card card-front card--tr">
  <div class="front-arc"></div>
  <div class="brand">
    <span class="brand-dot"></span>
    <div class="brand-name">The Steady Forge</div>
    <div class="brand-tagline">Steady steps, lasting change</div>
  </div>
  <div class="holder">
    <div class="holder-name">Ted Harlow</div>
    <div class="holder-credentials">CPC, CLHt, ATT, PNCP</div>
  </div>
  <ul class="contacts">
    <li class="contact">303-555-0147<svg class="contact-icon"><use href="#icon-phone"/></svg></li>
    <li class="contact">harlow.ted@thesteadyforge.example<svg class="contact-icon"><use href="#icon-mail"/></svg></li>
    <li class="contact">Box 4619, Millbrook, VT 05799-4619<svg class="contact-icon"><use href="#icon-pin"/></svg></li>
  </ul>
</section>

<section class="card card-front card--bl">
  <div class="front-arc"></div>
  <div class="brand">
    <span class="brand-dot"></span>
    <div class="brand-name">The Steady Forge</div>
    <div class="brand-tagline">Steady steps, lasting change</div>
  </div>
  <div class="holder">
    <div class="holder-name">Ted Harlow</div>
    <div class="holder-credentials">CPC, CLHt, ATT, PNCP</div>
  </div>
  <ul class="contacts">
    <li class="contact">303-555-0147<svg class="contact-icon"><use href="#icon-phone"/></svg></li>
    <li class="contact">harlow.ted@thesteadyforge.example<svg class="contact-icon"><use href="#icon-mail"/></svg></li>
    <li class="contact">Box 4619, Millbrook, VT 05799-4619<svg class="contact-icon"><use href="#icon-pin"/></svg></li>
  </ul>
</section>

<section class="card card-back card--br">
  <ul class="questions">
    <li class="question">If you were at your best,<br>what would<br>you do right now?</li>
    <li class="question">What is the decision<br>you have<br>been avoiding?</li>
    <li class="question">What's one action you<br>could take<br>in the next 10 minutes?</li>
  </ul>
</section>

</body>
</html>
```